Banner Ad Design

We require a banner ad design for 4 Brands.

Banner 1: Willowmere on the Heath
Please follow url http://www.goldenyearsresidences.example/index.php/willowmere-on-the-heath/welcome for art, logo, tagline.

Banner 2: Noble Brookhaven
Please follow url http://www.goldenyearsresidences.example/index.php/noble-brookhaven/welcome for art, logo, tagline.

Banner 3: Brookhaven Meadows
Please follow url http://www.goldenyearsresidences.example/index.php/brookhaven-meadows/welcome for art, logo, tagline.

Banner 4: Hartwell Court
http://www.goldenyearsresidences.example/index.php/hartwell-court/welcome

ALL Banners consists of - 1. LOGO, 2. TAGLINE: Experience and uncompromising Retirement Lifestyle. 3. CALL TO ACTION: View Images, Download the Brochure, Register for More.

Each brand must be broken into the following Sizes:

468 × 60
728 × 90
250 × 250
200 × 200
336 × 280
300 × 250
120 × 600
160 × 600
300 × 600
970 × 90
240 × 400
980 × 120
930 × 180
250 × 360
580 × 400
150kb max size

Target Market(s)

Seniors and their middle age children

Industry/Entity Type

Royal

Requirements
Must have
• 468 × 60
728 × 90
250 × 250
200 × 200
336 × 280
300 × 250
120 × 600
160 × 600
300 × 600
970 × 90
240 × 400
980 × 120
930 × 180
250 × 360
580 × 400
150kb max size
Nice to have
• large font for easy viewing - images of the experience
Should not have
• any pictures of decrepit people, or dying people - must be fun and vibrant.

```html
<!DOCTYPE html>
<html lang="en">
<head>
<meta charset="utf-8">
<title>Hartwell Court – Banner Set</title>
<link rel="stylesheet" href="https://fonts.googleapis.com/css2?family=Oswald:wght@400;500;600&display=swap">
<style>
  :root{
    --backdrop:#3a1f12;
    --navy-dark:#0b2158;
    --navy:#173f8e;
    --navy-light:#2a5db3;
    --gold:#f6b21c;
    --gold-deep:#e8860d;
    --white:#ffffff;
    --ink:#111111;
    --logo-blue:#17367a;
    --photo-leaf:#4f7a32;
    --photo-sky:#8fae6a;
    --photo-bloom:#d9507f;
  }
  *{box-sizing:border-box;margin:0;padding:0}
  html,body{width:1200px;height:837px;overflow:hidden}
  body{background:var(--backdrop);position:relative;font-family:"Oswald",sans-serif}

  .banner{position:absolute;overflow:hidden;background:linear-gradient(160deg,var(--navy-light),var(--navy) 45%,var(--navy-dark));box-shadow:0 0 0 1px rgba(0,0,0,.5)}
  .banner svg.art{position:absolute;inset:0;width:100%;height:100%}

  .logo-panel{position:absolute;background:var(--white);display:flex;align-items:center;justify-content:center;gap:10px}
  .logo-mark{width:12px;height:12px;border-radius:50%;background:var(--logo-blue);flex:none}
  .logo-name{font-family:"Oswald",sans-serif;font-weight:400;color:var(--logo-blue);line-height:1;white-space:nowrap}

  .line{position:absolute;left:0;right:0;text-align:center;text-transform:uppercase;line-height:1;white-space:nowrap;letter-spacing:-.2px}
  .line.lead{color:var(--white);font-weight:400}
  .line.accent{color:var(--gold);font-weight:600}

  .cta{position:absolute;display:flex;align-items:center;justify-content:space-between;padding:0 6px 0 10px;border-radius:4px;background:linear-gradient(#ffd24a,var(--gold) 45%,var(--gold-deep));color:var(--ink);font-weight:500;text-transform:uppercase;white-space:nowrap;box-shadow:0 1px 3px rgba(0,0,0,.5)}
  .cta-icon{width:16px;height:16px;border-radius:50%;background:var(--ink);display:flex;align-items:center;justify-content:center;flex:none;margin-left:6px}

  /* Skyscraper 160x600 */
  .skyscraper{left:48px;top:63px;width:201px;height:755px}
  .skyscraper .logo-panel{left:0;top:0;width:201px;height:88px}
  .skyscraper .logo-name{font-size:24px}

  /* Leaderboard 728x90 */
  .leaderboard{left:275px;top:64px;width:916px;height:110px}
  .leaderboard .logo-panel{left:0;top:0;width:210px;height:66px}
  .leaderboard .logo-name{font-size:22px}
  .leaderboard .line{left:auto;right:14px;text-align:right}

  /* Medium rectangle 336x280 */
  .rect-medium{left:276px;top:189px;width:421px;height:351px}
  .rect-medium .logo-panel{left:0;top:278px;width:421px;height:73px}
  .rect-medium .logo-name{font-size:28px}
  .rect-medium .line{left:208px;right:4px}

  /* Rectangle 300x250 */
  .rect-small{left:723px;top:227px;width:377px;height:313px}
  .rect-small .logo-panel{left:0;top:249px;width:377px;height:64px}
  .rect-small .logo-name{font-size:26px}
  .rect-small .line{left:192px;right:4px}
</style>
</head>
<body>

<!-- Skyscraper -->
<section class="banner skyscraper">
  <svg class="art" viewBox="0 0 201 755" preserveAspectRatio="none">
    <defs>
      <linearGradient id="garden-sky" x1="0" y1="0" x2="0" y2="1">
        <stop offset="0" stop-color="#9fb87a"/><stop offset=".5" stop-color="#c99a8a"/><stop offset="1" stop-color="#4a7a2e"/>
      </linearGradient>
    </defs>
    <path d="M0 88 H201 V500 Q100 470 0 540 Z" fill="url(#garden-sky)" role="img" aria-label="Smiling senior woman in a straw hat holding a pot of pink geraniums in a sunny garden"/>
    <path d="M0 540 Q100 470 201 500" fill="none" stroke="var(--gold)" stroke-width="5"/>
    <path d="M0 100 Q100 70 201 96" fill="none" stroke="var(--gold)" stroke-width="4"/>
  </svg>
  <div class="logo-panel"><span class="logo-mark"></span><span class="logo-name">Hartwell Court</span></div>
  <div class="line lead" style="top:555px;font-size:24px">Experience an</div>
  <div class="line lead" style="top:585px;font-size:24px">Uncompromising</div>
  <div class="line accent" style="top:618px;font-size:32px">&amp; Affordable</div>
  <div class="line accent" style="top:658px;font-size:38px">Retirement</div>
  <div class="line accent" style="top:702px;font-size:38px">Lifestyle</div>
  <div class="cta" style="left:20px;top:760px;width:162px;height:28px;font-size:13px">Register for more<span class="cta-icon"><svg width="8" height="8" viewBox="0 0 8 8"><path d="M2 1l4 3-4 3z" fill="#fff"/></svg></span></div>
</section>

<!-- Leaderboard -->
<section class="banner leaderboard">
  <svg class="art" viewBox="0 0 916 110" preserveAspectRatio="none">
    <defs>
      <linearGradient id="garden-wide" x1="0" y1="0" x2="1" y2="0">
        <stop offset="0" stop-color="#4a7a2e"/><stop offset=".5" stop-color="#c99a8a"/><stop offset="1" stop-color="#8fae6a"/>
      </linearGradient>
    </defs>
    <rect x="0" y="0" width="210" height="110" fill="var(--white)"/>
    <path d="M210 0 H520 Q480 60 440 110 H210 Z" fill="url(#garden-wide)" role="img" aria-label="Senior woman in a straw hat holding pink geraniums in a garden"/>
    <path d="M210 0 Q200 55 210 110" fill="none" stroke="var(--gold)" stroke-width="4"/>
    <path d="M520 0 Q480 60 440 110" fill="none" stroke="var(--gold)" stroke-width="5"/>
  </svg>
  <div class="logo-panel"><span class="logo-mark"></span><span class="logo-name">Hartwell Court</span></div>
  <div class="cta" style="left:18px;top:72px;width:158px;height:28px;font-size:12px">Register for more<span class="cta-icon"><svg width="8" height="8" viewBox="0 0 8 8"><path d="M2 1l4 3-4 3z" fill="#fff"/></svg></span></div>
  <div class="line lead" style="top:20px;font-size:28px">Experience an Uncompromising</div>
  <div class="line accent" style="top:56px;font-size:30px">&amp; Affordable Retirement Lifestyle</div>
</section>

<!-- Medium rectangle -->
<section class="banner rect-medium">
  <svg class="art" viewBox="0 0 421 351" preserveAspectRatio="none">
    <defs>
      <linearGradient id="garden-med" x1="0" y1="0" x2="0" y2="1">
        <stop offset="0" stop-color="#8fae6a"/><stop offset=".45" stop-color="#c99a8a"/><stop offset="1" stop-color="#4a7a2e"/>
      </linearGradient>
    </defs>
    <path d="M0 0 H215 Q240 140 150 278 H0 Z" fill="url(#garden-med)" role="img" aria-label="Senior woman in a straw hat holding pink geraniums in a garden"/>
    <path d="M215 0 Q240 140 150 278" fill="none" stroke="var(--gold)" stroke-width="5"/>
    <rect x="0" y="274" width="421" height="4" fill="var(--navy-dark)"/>
  </svg>
  <div class="line lead" style="top:18px;font-size:28px">Experience an</div>
  <div class="line lead" style="top:50px;font-size:28px">Uncompromising</div>
  <div class="line accent" style="top:85px;font-size:36px">&amp; Affordable</div>
  <div class="line accent" style="top:128px;font-size:40px">Retirement</div>
  <div class="line accent" style="top:172px;font-size:40px">Lifestyle</div>
  <div class="cta" style="left:143px;top:233px;width:179px;height:31px;font-size:14px">Register for more<span class="cta-icon"><svg width="8" height="8" viewBox="0 0 8 8"><path d="M2 1l4 3-4 3z" fill="#fff"/></svg></span></div>
  <div class="logo-panel"><span class="logo-mark"></span><span class="logo-name">Hartwell Court</span></div>
</section>

<!-- Rectangle -->
<section class="banner rect-small">
  <svg class="art" viewBox="0 0 377 313" preserveAspectRatio="none">
    <defs>
      <linearGradient id="garden-small" x1="0" y1="0" x2="0" y2="1">
        <stop offset="0" stop-color="#8fae6a"/><stop offset=".45" stop-color="#c99a8a"/><stop offset="1" stop-color="#4a7a2e"/>
      </linearGradient>
    </defs>
    <path d="M0 0 H190 Q212 125 135 249 H0 Z" fill="url(#garden-small)" role="img" aria-label="Senior woman in a straw hat holding pink geraniums in a garden"/>
    <path d="M190 0 Q212 125 135 249" fill="none" stroke="var(--gold)" stroke-width="5"/>
    <rect x="0" y="245" width="377" height="4" fill="var(--navy-dark)"/>
  </svg>
  <div class="line lead" style="top:12px;font-size:25px">Experience an</div>
  <div class="line lead" style="top:41px;font-size:25px">Uncompromising</div>
  <div class="line accent" style="top:74px;font-size:32px">&amp; Affordable</div>
  <div class="line accent" style="top:113px;font-size:36px">Retirement</div>
  <div class="line accent" style="top:153px;font-size:36px">Lifestyle</div>
  <div class="cta" style="left:193px;top:206px;width:159px;height:29px;font-size:13px">Register for more<span class="cta-icon"><svg width="8" height="8" viewBox="0 0 8 8"><path d="M2 1l4 3-4 3z" fill="#fff"/></svg></span></div>
  <div class="logo-panel"><span class="logo-mark"></span><span class="logo-name">Hartwell Court</span></div>
</section>

</body>
</html>
```